Business Card Design Project

I am a psychotherapist, counselor and expressive arts therapist (means I use every art form imaginable in the service of healing). I'm just starting out in private practice in San Francisco, CA. I work with individual adults, children and families. I'd like the card to mirror the simplicity and color palate of my website. I also would love if there is a symbol, image of fire, flame or spark (that is warming, not frightening).

Check out my website: www.lorabeckettmft.com

I want the cards to be printed in letter press so please keep that in mind!

Target Market(s)

Upper Middle Class Adults who are progressively minded, artistic or artists, open to psychotherapy, interested in health & healing.

Industry/Entity Type

Business

Requirements
Must have
• Text to be included:

Lora Beckett
Counseling, Psychotherapy & Expressive Arts

2814 Wexford Avenue, Suite F
San Francisco, CA 94127
p. 415.862.3097
lorajanebeckett@mailvane.net

www.lorabeckettmft.com

MFT License Number 68947

It's OK to abbreviate Number to # or Street to St., etc.

Must be compatible with letter press printing.
Nice to have
• I don't have a logo. I don't expect designers to necessarily create one for me, but if someone comes up with a simple image (see above about flame), that would be great. I don't have much of a budget now, but expect that to change in the next year or so and then could buy a logo for my website, future letterhead, etc.

```html
<!DOCTYPE html>
<html lang="en">
<head>
<meta charset="utf-8">
<title>Lora Beckett – Business Cards</title>
<link rel="stylesheet" href="https://fonts.googleapis.com/css2?family=Tinos:ital,wght@0,400;1,400;1,700&display=swap">
<style>
  :root {
    --backdrop: #d9d2c3;
    --metal-light: #f4f4f4;
    --metal-mid: #c9c9c9;
    --metal-dark: #8c8c8c;
    --name-rose: #d83a5c;
    --tagline-grey: #4a4a4a;
    --contact-grey: #3d3d3d;
    --ornament-gold-1: #e9b81f;
    --ornament-gold-2: #8a5a14;
    --ornament-silver-1: #e8e8e8;
    --ornament-silver-2: #a9a9a9;
  }
  * { box-sizing: border-box; margin: 0; padding: 0; }
  html, body {
    width: 1200px; height: 902px; overflow: hidden;
    background: var(--backdrop);
  }
  .sheet { position: relative; width: 1200px; height: 902px; }
  .card {
    position: absolute;
    width: 544px; height: 310px;
    background:
      radial-gradient(ellipse 60% 70% at 50% 50%, var(--metal-light) 0%, var(--metal-mid) 65%, var(--metal-dark) 100%);
    font-family: "Tinos", "Times New Roman", serif;
    text-align: center;
  }
  .card--gold { left: 335px; top: 151px; }
  .card--silver { left: 338px; top: 485px; }
  .ornament {
    position: absolute; left: 145px; width: 254px; height: 42px;
    border-radius: 21px;
  }
  .ornament--top { top: 44px; }
  .ornament--bottom { top: 160px; }
  .card--gold .ornament {
    background: linear-gradient(180deg, var(--ornament-gold-1), var(--ornament-gold-2));
    opacity: .55;
  }
  .card--silver .ornament {
    background: linear-gradient(180deg, var(--ornament-silver-1), var(--ornament-silver-2));
    opacity: .7;
  }
  .card__name {
    position: absolute; left: 0; right: 0; top: 88px;
    font-style: italic; font-weight: 400;
    font-size: 37px; letter-spacing: 1px;
    color: var(--name-rose);
    text-shadow: 0 1px 0 rgba(255,255,255,.6), 0 -1px 0 rgba(0,0,0,.25);
  }
  .card__tagline {
    position: absolute; left: 0; right: 0; top: 132px;
    font-style: italic; font-weight: 700; font-size: 13.5px;
    color: var(--tagline-grey);
  }
  .card__contact {
    position: absolute; left: 0; right: 0; top: 228px;
    font-size: 14.5px; line-height: 19.5px;
    color: var(--contact-grey);
    text-shadow: 0 1px 0 rgba(255,255,255,.5);
  }
</style>
</head>
<body>
<main class="sheet">
  <section class="card card--gold">
    <div class="ornament ornament--top" role="img" aria-label="Gold flourish scroll ornament"></div>
    <h1 class="card__name">LORA BECKETT</h1>
    <p class="card__tagline">Counseling, Psychotherapy &amp; Expressive Arts</p>
    <div class="ornament ornament--bottom" role="img" aria-label="Gold flourish scroll ornament"></div>
    <address class="card__contact" style="font-style:normal">
      2814 Wexford Avenue, Suite F. San Francisco, CA 94127<br>
      p. 415.862.3097 | lorajanebeckett@mailvane.net<br>
      www.lorabeckettmft.com
    </address>
  </section>

  <section class="card card--silver">
    <div class="ornament ornament--top" role="img" aria-label="Silver embossed flourish scroll ornament"></div>
    <h2 class="card__name">LORA BECKETT</h2>
    <p class="card__tagline">Counseling, Psychotherapy &amp; Expressive Arts</p>
    <div class="ornament ornament--bottom" role="img" aria-label="Silver embossed flourish scroll ornament"></div>
    <address class="card__contact" style="font-style:normal">
      2814 Wexford Avenue, Suite F. San Francisco, CA 94127<br>
      p. 415.862.3097 | lorajanebeckett@mailvane.net<br>
      www.lorabeckettmft.com
    </address>
  </section>
</main>
</body>
</html>
```